Business Card Design

The name of my business is called Amber Lantern, Inc.

We are the first brick and mortar store in our state that will specialize in spy equipment. I don't want the term "spy equipment" used in the design of the card. I would like a double sided card with the one side having all my contact information and the other side having the company name and the quote "Discreet Surveillance Equipment". I'm not looking for the perfect card on the first try but am not looking to make many changes.

I would like the card to speak sophistication so I tend to lean toward dark color backgrounds.

Industry/Entity Type

Store

Contact Information for Business Card

Gerald Moravec, Consultant
483-917-6052
gerald.moravec@amberlantern.net
www.amberlantern.net

```html
<!DOCTYPE html>
<html lang="en">
<head>
<meta charset="utf-8">
<title>Amber Lantern, Inc. — Business Card</title>
<link rel="stylesheet" href="https://fonts.googleapis.com/css2?family=Mulish:ital,wght@0,400;0,700;1,400&display=swap">
<style>
  :root {
    --page: #ffffff;
    --card-black: #000000;
    --panel-grey: #3d3d3e;
    --mark-grey: #c9c9c9;
    --ink-white: #ffffff;
    --shadow: rgba(0, 0, 0, 0.45);
    --font-main: "Mulish", "Century Gothic", sans-serif;
  }
  * { margin: 0; padding: 0; box-sizing: border-box; }
  html, body {
    width: 1200px;
    height: 1000px;
    overflow: hidden;
    background: var(--page);
    font-family: var(--font-main);
    color: var(--ink-white);
  }
  .canvas { position: relative; width: 1200px; height: 1000px; }
  .card {
    position: absolute;
    left: 250px;
    width: 688px;
    background: var(--card-black);
    box-shadow: 6px 7px 9px var(--shadow);
    overflow: hidden;
  }
  .card--front { top: 86px; height: 391px; }
  .card--back { top: 529px; height: 388px; }

  .mark-dot { position: absolute; display: block; }
  .mark-dot circle { fill: var(--mark-grey); stroke: var(--ink-white); stroke-width: 4; }

  .wordmark-part {
    position: absolute;
    font-weight: 400;
    white-space: nowrap;
    line-height: 1;
  }

  /* Front */
  .tagline-panel {
    position: absolute;
    right: 0; top: 0;
    width: 249px; height: 261px;
    background: var(--panel-grey);
    padding: 72px 0 0 30px;
  }
  .tagline { font-size: 27px; line-height: 32px; font-weight: 400; letter-spacing: 0.3px; }
  .card--front .mark-dot { left: 178px; top: 118px; width: 172px; height: 172px; }
  .card--front .wordmark-part { top: 297px; font-size: 52px; }
  .card--front .wordmark-part--lead { left: 37px; }
  .card--front .wordmark-part--tail { left: 343px; }

  /* Back */
  .web-band {
    position: absolute;
    left: 0; top: 0;
    width: 100%; height: 123px;
    background: var(--panel-grey);
    text-align: center;
    padding-top: 36px;
    font-size: 21px;
    line-height: 27px;
    letter-spacing: 0.2px;
  }
  .contact { position: absolute; left: 396px; top: 150px; }
  .contact__name { font-size: 24px; font-weight: 700; line-height: 1.1; }
  .contact__role { font-size: 17px; font-style: italic; margin-top: 2px; }
  .contact__phone { font-size: 20px; margin-top: 22px; letter-spacing: 0.3px; }
  .card--back .mark-dot { left: 154px; top: 178px; width: 128px; height: 128px; }
  .card--back .wordmark-part { top: 308px; font-size: 43px; }
  .card--back .wordmark-part--lead { left: 35px; }
  .card--back .wordmark-part--tail { left: 275px; }
</style>
</head>
<body>
  <main class="canvas">
    <section class="card card--front" aria-label="Business card front">
      <div class="tagline-panel">
        <p class="tagline">Discreet<br>Surveillance<br>Equipment</p>
      </div>
      <svg class="mark-dot" viewBox="0 0 172 172" aria-hidden="true"><circle cx="86" cy="86" r="82"/></svg>
      <p class="wordmark" aria-label="Amber Lantern">
        <span class="wordmark-part wordmark-part--lead">Amber</span>
        <span class="wordmark-part wordmark-part--tail">Lantern</span>
      </p>
    </section>

    <section class="card card--back" aria-label="Business card back">
      <div class="web-band">
        <p class="email">gerald.moravec@amberlantern.net</p>
        <p class="website">www.amberlantern.net</p>
      </div>
      <div class="contact">
        <p class="contact__name">Gerald Moravec</p>
        <p class="contact__role">Consultant</p>
        <p class="contact__phone">483-917-6052</p>
      </div>
      <svg class="mark-dot" viewBox="0 0 128 128" aria-hidden="true"><circle cx="64" cy="64" r="60"/></svg>
      <p class="wordmark" aria-label="Amber Lantern, Inc">
        <span class="wordmark-part wordmark-part--lead">Amber</span>
        <span class="wordmark-part wordmark-part--tail">Lantern, Inc</span>
      </p>
    </section>
  </main>
</body>
</html>
```